Subscription Box Company Needs a Boxwren Box Design

WE NEED 5 sides of a 10" x 4" x 8" box designed.
Not one entire design, should be simple with 5 images or designs within one project. Visit boxwren.com to see what we mean.

What we need:
We send our subscribers new and unique products and we want a box that conveys professional yet fun and exciting feelings. We want our logo (attached) and our website (zorvat.com) listed somewhere. The rest is up to you!

WHAT WE NEED FROM YOU:
Go to boxwren.com and select their mailer box, then select their 10" x 8" x 4" mailer box with a white background. We need your design to be able to upload on each side of the box - so we can just take your design and upload it on their website. That simple!

Please follow the directions above!

From Boxwren :

Color Settings

Your artwork can be either CMYK or RGB, but we would highly encourage you to convert your images into CMYK before making your order. This allows you to ‘soft-proof’ your images on screen and see how the colors will look. If you supply your images in RGB they will be automatically converted to CMYK. RGB colors may appear duller or desaturated when printed (and we’re sure you don’t want that).

Design Formats

Any non-photographic content (including graphics and text) are best sent to us as vector based PDFs or Adobe Illustrator (.ai) files. These make your lines crisp and clear.

Please make sure there are no cut or crop lines, all transparencies have been flattened, and any fonts are embedded (or outlined) before saving your designs. To do that in Adobe Illustrator, select all text and choose Type > Create Outlines.

Design Typography, Text and Line Art

Just a few *important* points:

Text should be at least 14pt - regardless of how it looks on screen, any smaller and it won’t print well on corrugate.
Try to keep text in bold weights and colors.
If any of your lines are in a solid or dark color, make sure they’re no thinner than 2pt.
All fonts should be outlined/vectorized.

Industry/Entity Type

It Company

Colors
0592cd
ffffff
33a6d7
85cae6
cee9f5

Requirements
Must have
• Our logo, and our website zorvat.com listed somewhere.
Nice to have
• Anything!
Should not have
• Nothing to masculine or feminine, we want it gender neutral.

```html
<!DOCTYPE html>
<html lang="en">
<head>
<meta charset="utf-8">
<title>Zorvat Mailer Box – Dieline Artwork</title>
<link href="https://fonts.googleapis.com/css2?family=Archivo:wght@400;900&display=swap" rel="stylesheet">
<style>
  :root {
    --brand-blue: #0592cd;
    --logo-blue: #33a6d7;
    --headline-blue: #1f8cba;
    --ray-blue: #85cae6;
    --ray-pale: #cee9f5;
    --panel-white: #ffffff;
    --stage: #e9ecee;
  }
  * { margin: 0; padding: 0; box-sizing: border-box; }
  html, body { width: 1200px; height: 878px; overflow: hidden; }
  body {
    background: var(--stage);
    position: relative;
    font-family: "Archivo", Arial, sans-serif;
  }
  .box-net { position: absolute; left: 0; top: 0; width: 1200px; height: 878px; }

  .panel {
    position: absolute;
    background: var(--panel-white);
    overflow: hidden;
  }
  .panel::after {
    content: "";
    position: absolute;
    inset: 5px;
    border: 3px solid var(--brand-blue);
    border-radius: 6px;
    pointer-events: none;
  }
  .panel--top    { left: 212px; top: 14px;  width: 466px; height: 184px; }
  .panel--left   { left: 22px;  top: 204px; width: 186px; height: 374px; }
  .panel--center { left: 212px; top: 204px; width: 466px; height: 374px; }
  .panel--right  { left: 686px; top: 204px; width: 186px; height: 374px; }
  .panel--bottom { left: 212px; top: 586px; width: 466px; height: 184px; }

  .ray-field {
    position: absolute;
    inset: 8px;
    background: radial-gradient(ellipse at 50% 45%, var(--panel-white) 0%, var(--ray-pale) 55%, var(--ray-blue) 100%);
    opacity: 0.55;
  }

  .face {
    position: absolute;
    left: 50%; top: 50%;
    display: flex;
    align-items: center;
    justify-content: center;
  }
  .face--upright  { width: 466px; height: 184px; transform: translate(-50%, -50%); }
  .face--flipped  { width: 466px; height: 184px; transform: translate(-50%, -50%) rotate(180deg); }
  .face--turn-cw  { width: 374px; height: 186px; transform: translate(-50%, -50%) rotate(90deg); }
  .face--turn-ccw { width: 374px; height: 186px; transform: translate(-50%, -50%) rotate(-90deg); }

  .brand-name {
    font-family: "Archivo", Arial, sans-serif;
    font-weight: 900;
    color: var(--logo-blue);
    letter-spacing: -1px;
    line-height: 1;
    display: flex;
    align-items: center;
    gap: 12px;
  }
  .brand-name__dot {
    width: 18px; height: 18px;
    border-radius: 50%;
    background: var(--logo-blue);
  }
  .brand-name--end { font-size: 88px; }
  .brand-name--side { font-size: 72px; }
  .brand-name--hero { font-size: 96px; }

  .face--hero {
    width: 466px; height: 374px;
    transform: translate(-50%, -50%);
    flex-direction: column;
    justify-content: flex-start;
  }
  .face--hero .brand-name { margin-top: 80px; }
  .tagline {
    margin-top: 52px;
    font-weight: 900;
    font-size: 33px;
    color: var(--headline-blue);
    letter-spacing: 0.5px;
  }
  .contents-row {
    width: 400px;
    margin-top: 10px;
    display: flex;
    align-items: flex-end;
    justify-content: space-between;
  }
  .contents-icon { width: 58px; height: 58px; fill: var(--brand-blue); }
  .contents-icon--line { fill: none; stroke: var(--brand-blue); stroke-width: 3; }
  .site-url {
    font-weight: 400;
    font-size: 37px;
    color: var(--logo-blue);
    margin-bottom: 2px;
  }
</style>
</head>
<body>
<main class="box-net">

  <section class="panel panel--top" aria-label="Top flap">
    <div class="ray-field" role="img" aria-label="Light blue sunburst ray pattern"></div>
    <div class="face face--flipped">
      <div class="brand-name brand-name--end"><span class="brand-name__dot"></span>zorvat</div>
    </div>
  </section>

  <section class="panel panel--left" aria-label="Left side">
    <div class="ray-field" role="img" aria-label="Light blue sunburst ray pattern"></div>
    <div class="face face--turn-cw">
      <div class="brand-name brand-name--side"><span class="brand-name__dot"></span>zorvat</div>
    </div>
  </section>

  <section class="panel panel--center" aria-label="Lid">
    <div class="ray-field" role="img" aria-label="Light blue sunburst ray pattern"></div>
    <div class="face face--hero">
      <div class="brand-name brand-name--hero"><span class="brand-name__dot"></span>zorvat</div>
      <p class="tagline">What’s in the box?</p>
      <div class="contents-row">
        <svg class="contents-icon" viewBox="0 0 60 60" aria-label="T-shirt">
          <path d="M20 6 L8 12 L2 26 L12 30 L14 24 L14 56 L46 56 L46 24 L48 30 L58 26 L52 12 L40 6 C37 12 23 12 20 6 Z"/>
        </svg>
        <svg class="contents-icon" viewBox="0 0 60 60" aria-label="Headphones">
          <path d="M8 40 V32 A22 22 0 0 1 52 32 V40" fill="none" stroke="var(--brand-blue)" stroke-width="5"/>
          <rect x="4" y="36" width="11" height="18" rx="4"/>
          <rect x="45" y="36" width="11" height="18" rx="4"/>
          <path d="M27 22 V42 M27 22 L36 20 V38" fill="none" stroke="var(--brand-blue)" stroke-width="3"/>
          <circle cx="24" cy="43" r="4"/><circle cx="33" cy="39" r="4"/>
        </svg>
        <span class="site-url">zorvat.com</span>
        <svg class="contents-icon" viewBox="0 0 60 60" aria-label="Tablet">
          <rect class="contents-icon--line" x="14" y="4" width="32" height="48" rx="4"/>
          <circle cx="30" cy="47" r="2"/>
        </svg>
        <svg class="contents-icon" viewBox="0 0 60 60" aria-label="Gift">
          <rect x="6" y="20" width="48" height="12"/>
          <rect x="10" y="34" width="40" height="24"/>
          <rect x="27" y="20" width="6" height="38" fill="var(--panel-white)"/>
          <path d="M30 20 C22 6 12 10 18 18 Z M30 20 C38 6 48 10 42 18 Z" fill="none" stroke="var(--brand-blue)" stroke-width="3"/>
        </svg>
      </div>
    </div>
  </section>

  <section class="panel panel--right" aria-label="Right side">
    <div class="ray-field" role="img" aria-label="Light blue sunburst ray pattern"></div>
    <div class="face face--turn-ccw">
      <div class="brand-name brand-name--side"><span class="brand-name__dot"></span>zorvat</div>
    </div>
  </section>

  <section class="panel panel--bottom" aria-label="Front side">
    <div class="ray-field" role="img" aria-label="Light blue sunburst ray pattern"></div>
    <div class="face face--upright">
      <div class="brand-name brand-name--end"><span class="brand-name__dot"></span>zorvat</div>
    </div>
  </section>

</main>
</body>
</html>
```